Very visible CoWorking Building Sign overlooking downtown LA and 110 freeway

Our building is drab but very visible and in the best location. We need a great sign for our monolith that overlooks downtown LA and the 100 freeway. We are a new CoWorking business and would like to have a few things we do on the sign: private offices, virtual offices, CoWorking Lounge. Everything we have seen is ho-hum. Can you get us noticed? We need people to know what we do and that we are here but in a creative, professional, unique sign.
Target Market(s)
People who have a business in DTLA, remote workers and those who work from home who need a professional address.
Requirements
Must have
- Our logo (which can be somewhat reimagined) which has our address 2740 on it. The three things we focus on: Private Offices, Virtual Offices, CoWorking Lounge. Incorporate some Navy. Readable from several hundred feet away.
Nice to have
- Mural feel? Something inspirational in this crazy COVID times? Graphics? Color block. I like the idea of decorative but it has to be readable as a building sign. The same with the use of colors. Our colors are grays and navy but with a pop of the chartreuse (we have 2 velvet chartreuse chairs in the space). Helpful to view our website: Halvorn2740.com.
Should not have
- Not too graffiti. Keep it professional but unique and wow.

```html
<!DOCTYPE html>
<html lang="en">
<head>
<meta charset="utf-8">
<title>2740 Halvorn — Building Sign</title>
<link href="https://fonts.googleapis.com/css2?family=Aleo:wght@700&family=Josefin+Sans:wght@600&display=swap" rel="stylesheet">
<style>
  :root {
    --navy: #1c2b55;
    --white: #ffffff;
    --rule-gray: #8f9298;
    --band-gray: #c9cbce;
    --backdrop: #e6e7e9;
    --photo-warm: #b9ad8f;
    --photo-light: #e4e6e2;
    --chartreuse: #8d9a2c;
  }
  * { margin: 0; padding: 0; box-sizing: border-box; }
  html, body {
    width: 1200px;
    height: 801px;
    overflow: hidden;
    background: var(--backdrop);
  }
  .sign {
    position: absolute;
    left: 40px;
    top: 100px;
    width: 1120px;
    height: 600px;
    box-shadow: 0 6px 18px rgba(0,0,0,0.18);
  }
  .sign svg { display: block; }
  .brand {
    font-family: "Josefin Sans", sans-serif;
    font-weight: 600;
    fill: var(--navy);
  }
  .service {
    font-family: "Aleo", serif;
    font-weight: 700;
    fill: var(--navy);
  }
</style>
</head>
<body>
  <div class="sign">
    <svg width="1120" height="600" viewBox="0 0 1120 600" xmlns="http://www.w3.org/2000/svg">
      <defs>
        <linearGradient id="lounge-tones" x1="0" y1="0" x2="1" y2="1">
          <stop offset="0" stop-color="var(--photo-light)"/>
          <stop offset="0.45" stop-color="var(--photo-warm)"/>
          <stop offset="0.75" stop-color="var(--chartreuse)"/>
          <stop offset="1" stop-color="#6f6a52"/>
        </linearGradient>
      </defs>

      <!-- lounge photo area -->
      <rect class="lounge-photo" x="440" y="0" width="680" height="600" fill="url(#lounge-tones)"
            role="img" aria-label="Photo of the coworking lounge with two chartreuse velvet armchairs, plants and a round rug"/>

      <!-- navy accent stripes -->
      <polygon class="accent-stripe" points="790,0 840,0 1050,600 990,600" fill="var(--navy)" opacity="0.75"/>
      <polygon class="accent-stripe" points="890,0 1120,0 1120,600 1100,600" fill="var(--navy)" opacity="0.85"/>

      <!-- white text panel -->
      <polygon class="text-panel" points="0,0 490,0 714,600 0,600" fill="var(--white)"/>
      <polygon class="base-band" points="0,552 696,552 714,600 0,600" fill="var(--band-gray)"/>

      <!-- brand name -->
      <text class="brand" x="72" y="168" font-size="64" letter-spacing="2">2740 HALVORN</text>

      <!-- divider rule -->
      <line x1="0" y1="198" x2="560" y2="228" stroke="var(--rule-gray)" stroke-width="4"/>

      <!-- services -->
      <g class="service-item">
        <circle cx="92" cy="296" r="21" fill="none" stroke="var(--navy)" stroke-width="4"/>
        <path d="M80 296 H102 M94 287 L103 296 L94 305" fill="none" stroke="var(--navy)" stroke-width="5" stroke-linecap="round" stroke-linejoin="round"/>
        <text class="service" x="136" y="314" font-size="52">Private Offices</text>
      </g>
      <g class="service-item">
        <circle cx="92" cy="376" r="21" fill="none" stroke="var(--navy)" stroke-width="4"/>
        <path d="M80 376 H102 M94 367 L103 376 L94 385" fill="none" stroke="var(--navy)" stroke-width="5" stroke-linecap="round" stroke-linejoin="round"/>
        <text class="service" x="136" y="394" font-size="52">Virtual Offices</text>
      </g>
      <g class="service-item">
        <circle cx="92" cy="456" r="21" fill="none" stroke="var(--navy)" stroke-width="4"/>
        <path d="M80 456 H102 M94 447 L103 456 L94 465" fill="none" stroke="var(--navy)" stroke-width="5" stroke-linecap="round" stroke-linejoin="round"/>
        <text class="service" x="136" y="474" font-size="52">CoWorking Lounge</text>
      </g>
    </svg>
  </div>
</body>
</html>
```